The Vixen Rides Again Line of Sparkling Wine & Spirits

Back info: Tara Rose Whitfield Owner 209-555-0143 1480 E. Harlow Rd, Bldg. 7, & 8, Vinehaven Ca. 95299
Sparkling Wines & Collectibles www.thevixenridesagain.example
Ok I have uploaded the winning design. The color that I am after is the Fushia, Raspberry, Red, Matte Satin Matalic Finish. With a 24 Karet Gold color Foil. The Bottle is on the top row and it's the 2nd Bottle in. That is the Color that I want. This is the style of font. Make sure that you put what we're advertising. Good Luck to you all. Warmest regards, Tara
Target Market(s)
21 & up UniSex
Industry/Entity Type
Sparkling Wine and Memorabilia
Contact Information for Business Card
there listed up above.....

```html
<!DOCTYPE html>
<html lang="en">
<head>
<meta charset="utf-8">
<title>The Vixen Rides Again – Business Card</title>
<link rel="stylesheet" href="https://fonts.googleapis.com/css2?family=Cinzel:wght@500&family=Marcellus&display=swap">
<style>
  :root {
    --stage: #3b3b3d;
    --fuchsia: #dc1489;
    --fuchsia-deep: #9a0f5c;
    --gold: #d6ad3e;
    --gold-light: #f2d77a;
    --gold-dark: #a27a1f;
    --ink: #1f1f1f;
    --white: #ffffff;
  }
  * { box-sizing: border-box; margin: 0; padding: 0; }
  html, body { width: 1200px; height: 1200px; overflow: hidden; background: var(--stage); }
  .stage {
    width: 1200px; height: 1200px;
    display: flex; flex-direction: column; align-items: center; justify-content: center; gap: 52px;
  }
  .card {
    position: relative; width: 900px; height: 514px; border-radius: 34px; overflow: hidden;
    background: radial-gradient(ellipse at 50% 45%, var(--fuchsia) 0%, #c8117c 55%, var(--fuchsia-deep) 100%);
    box-shadow: 0 0 0 3px var(--gold), 0 18px 40px rgba(0,0,0,.55);
    font-family: "Marcellus", serif;
  }
  /* front */
  .contact { position: absolute; left: 56px; top: 60px; color: var(--white); }
  .contact__name { font-size: 44px; color: var(--gold); line-height: 1; }
  .contact__role { font-size: 17px; letter-spacing: 1px; margin: 4px 0 24px; }
  .contact__row { display: flex; align-items: flex-start; gap: 14px; font-size: 23px; line-height: 1.2; margin-bottom: 12px; }
  .contact__row svg { flex: none; width: 24px; height: 24px; margin-top: 2px; }
  .social { display: flex; gap: 12px; margin: 14px 0 0 38px; }
  .social span { width: 28px; height: 28px; border-radius: 50%; background: var(--gold); }
  .brand { position: absolute; right: 60px; top: 70px; width: 380px; text-align: center; }
  .brand__name { font-size: 44px; line-height: 1.05; color: var(--gold); }
  .brand__tagline { font-family: "Cinzel", serif; font-weight: 500; font-size: 19px; line-height: 1.15; color: var(--ink); margin-top: 26px; letter-spacing: 1px; }
  .gold-rule { position: absolute; left: 0; right: 0; top: 376px; height: 12px;
    background: linear-gradient(90deg, var(--gold-dark), var(--gold-light) 50%, var(--gold-dark)); }
  .pattern-band { position: absolute; left: 0; right: 0; top: 388px; bottom: 0;
    background: linear-gradient(90deg, #6e1245, #2a1a22 50%, #6e1245); }
  /* back */
  .card--back { display: flex; align-items: center; justify-content: center; }
  .card--back .brand__name { font-size: 66px; }
</style>
</head>
<body>
<main class="stage">
  <section class="card card--front">
    <div class="contact">
      <p class="contact__name">Tara Rose Whitfield</p>
      <p class="contact__role">OWNER</p>
      <p class="contact__row">
        <svg viewBox="0 0 24 24"><path fill="#d6ad3e" d="M6.6 10.8a15 15 0 0 0 6.6 6.6l2.2-2.2c.3-.3.7-.4 1-.2 1.1.4 2.3.6 3.6.6.6 0 1 .4 1 1V20c0 .6-.4 1-1 1A17 17 0 0 1 3 4c0-.6.4-1 1-1h3.5c.6 0 1 .4 1 1 0 1.3.2 2.5.6 3.6.1.3 0 .7-.2 1z"/></svg>
        209-555-0143
      </p>
      <p class="contact__row">
        <svg viewBox="0 0 24 24" fill="none" stroke="#d6ad3e" stroke-width="1.8"><circle cx="12" cy="12" r="9"/><path d="M3 12h18M12 3c3 3 3 15 0 18M12 3c-3 3-3 15 0 18"/></svg>
        www.thevixenridesagain.example
      </p>
      <p class="contact__row">
        <svg viewBox="0 0 24 24"><path fill="#d6ad3e" d="M12 2a7 7 0 0 0-7 7c0 5 7 13 7 13s7-8 7-13a7 7 0 0 0-7-7zm0 9.5A2.5 2.5 0 1 1 12 6.5a2.5 2.5 0 0 1 0 5z"/></svg>
        <span>1480 E. Harlow Rd, Bldg. 7, &amp; 8,<br>Vinehaven Ca. 95299<br>Sparkling Wines &amp; Collectibles</span>
      </p>
      <div class="social"><span></span><span></span></div>
    </div>
    <div class="brand">
      <p class="brand__name">The Vixen Rides Again</p>
      <p class="brand__tagline">LINE OF SPARKLING<br>WINE &amp; SPIRITS</p>
    </div>
    <div class="gold-rule"></div>
    <div class="pattern-band" role="img" aria-label="Decorative black lattice pattern on fuchsia"></div>
  </section>

  <section class="card card--back">
    <p class="brand__name">The Vixen Rides Again</p>
  </section>
</main>
</body>
</html>
```